The Online Growth Blueprint for Garden & Patio Building Crews

We need a book cover design that is for a book targeting landscape and outdoor living contractors that helps them grow their business using online marketing.

We run a business focused on this industry so you can see what we do: https://gardencrewpromo.com/

The title is: The Online Growth Blueprint for Garden & Patio Building Crews

The author is: Trent Halvorsen
Some drafts have been done however they're still looking basic and somewhat amateur, we're looking for something that will stand out.

Target Market(s)

Landscape, Hardscape and Outdoor Living Contractors and Business Owners

Industry/Entity Type

Online Marketing

Font styles to use
Serif
Sans Serif

Requirements
Must have
• The part of the title that should stand out the most is the text "Online Growth Blueprint".
Should not have
• The color red

```html
<!DOCTYPE html>
<html lang="en">
<head>
<meta charset="utf-8">
<title>The Online Growth Blueprint for Garden &amp; Patio Building Crews — Book Cover</title>
<link rel="stylesheet" href="https://fonts.googleapis.com/css2?family=Anton&family=Oswald:wght@600&family=Playfair+Display:ital,wght@1,700&display=swap">
<style>
  :root {
    --stage: #1f1f1f;
    --sky-top: #1b2c40;
    --sky-mid: #245b8f;
    --sky-low: #5f9bcc;
    --sky-haze: #b6d3e8;
    --lime: #a6c617;
    --white: #ffffff;
    --badge: #1e2b36;
  }
  * { margin: 0; padding: 0; box-sizing: border-box; }
  html, body {
    width: 1200px; height: 1200px; overflow: hidden;
    background: var(--stage);
  }
  .cover {
    position: absolute; left: 215px; top: 23px;
    width: 770px; height: 1154px; overflow: hidden;
    background: linear-gradient(180deg, var(--sky-top) 0%, #1f3f62 22%, var(--sky-mid) 45%, var(--sky-low) 62%, var(--sky-haze) 72%);
  }
  .cover__author {
    position: absolute; top: 76px; left: 329px; width: 300px;
    text-align: center; white-space: nowrap;
    font-family: "Oswald", sans-serif; font-weight: 600;
    font-size: 26px; line-height: 34px; letter-spacing: 3px; color: var(--white);
  }
  .cover__title { position: absolute; left: 0; top: 0; width: 770px; height: 760px; }
  .cover__title text { font-family: "Anton", sans-serif; }
  .title--white { fill: var(--white); }
  .title--lime { fill: var(--lime); }
  .subtitle { fill: var(--white); }
  .subtitle__amp { font-family: "Playfair Display", serif; font-style: italic; font-weight: 700; }
  .cover__scene {
    position: absolute; left: 0; bottom: 0; width: 100%; height: 420px;
    background:
      linear-gradient(180deg, rgba(182,211,232,0) 0%, #a8c6d8 18%, #7d9a80 38%, #3f5c36 52%, #6b5a48 66%, #4c8fa3 78%, #8a6a4f 100%);
  }
  .cover__badge {
    position: absolute; left: 623px; top: 1011px;
    width: 114px; height: 114px; background: var(--badge);
    display: flex; align-items: center; justify-content: center;
    text-align: center; padding: 10px;
    font-family: "Oswald", sans-serif; font-weight: 600;
    font-size: 15px; line-height: 18px; letter-spacing: 1px;
    color: var(--lime);
  }
</style>
</head>
<body>
  <main class="cover">
    <div class="cover__scene" role="img" aria-label="Photo of a modern backyard with a slatted pergola over a wooden deck, lounge furniture, a rectangular pool and a row of evergreen shrubs under a blue sky"></div>

    <p class="cover__author">TRENT HALVORSEN</p>

    <svg class="cover__title" viewBox="0 0 770 760" aria-label="The Online Growth Blueprint for Garden and Patio Building Crews">
      <text class="title--white" x="89" y="247" font-size="98" textLength="146" lengthAdjust="spacingAndGlyphs">THE</text>
      <text class="title--lime" x="248" y="247" font-size="136" textLength="431" lengthAdjust="spacingAndGlyphs">ONLINE</text>
      <text class="title--lime" x="52" y="385" font-size="136" textLength="668" lengthAdjust="spacingAndGlyphs">GROWTH</text>
      <text class="title--lime" x="52" y="523" font-size="136" textLength="668" lengthAdjust="spacingAndGlyphs">BLUEPRINT</text>

      <text class="subtitle" x="385" y="617" font-size="76" text-anchor="middle">FOR GARDEN <tspan class="subtitle__amp">&amp;</tspan> PATIO</text>
      <text class="subtitle" x="385" y="707" font-size="76" text-anchor="middle">BUILDING CREWS</text>
    </svg>

    <div class="cover__badge">GARDEN CREW PROMO</div>
  </main>
</body>
</html>
```